Veterinary Hospital Brochure - 2 Drafts - 1 Normal and 1 Fun.

Fernvale Pet Hospital needs a brochure to promote our veterinary hospital. These will be delivered to local mailboxes. I would like to see atleast 2 submissions from each designer.
One submission conservative and A4 folded DL and another submission more radical and interesting with innovative folding or crazy concepts. Maybe the brochure could be designed to fold into a dog house ?
I want at least one version to be VERY SIMPLE AND INTIMATE.
Our existing website is here: http://fernvalepet.com/ and our new website will look like this: http://demo1.plomtrava.ru/#home
Please use colors and images from the new website, and information from the old website. The heading font used in the new site is Zetafonts - Kitten Slant Monoline
I want the brochure to be simple and engaging on first view, and then provide the opportunity to find more information if desired. The brochure needs to be captivating on the outside so people don't throw it away immediately.

We will soon need letterhead, flags, pens, business cards, signs and vouchers so there is the opportunity for more work for the successful designer.

Target Market(s)

Women 25 to 44

Industry/Entity Type

Veterinary

Contact Information for Business Card

Fernvale Pet Hospital
14 Quorra Court
Brackenridge
NSW 2418
Phone: 02 61947203
Emergency: 0417380562
Fax: 02 83516094
www.fernvalepethospital.com.au
contact@fernvalepethospital.com.au

Font styles to use
Script

Requirements
Must have
• Colors from the new website: http://fernvalepethospital.com.au/ and new logo.
• Information from the old website: http://fernvalepet.com/
• 2 drafts - A normal A4 folded DL flyer and an interesting crazy design.
Nice to have
• VERY SIMPLE
• Subdued
• Intimate
Should not have
• Intense colours
• Red

```html
<!DOCTYPE html>
<html lang="en">
<head>
<meta charset="utf-8">
<title>Fernvale Pet Hospital – Tri-fold Brochure</title>
<link href="https://fonts.googleapis.com/css2?family=Josefin+Sans:wght@400;700&family=Sriracha&display=swap" rel="stylesheet">
<style>
  :root {
    --orange: #f58a1f;
    --orange-soft: #f7a04a;
    --brown: #6e4519;
    --brown-deep: #55340f;
    --brown-text: #5a3a1c;
    --green: #8cc63f;
    --green-dark: #2f4a10;
    --paper: #ffffff;
    --stage: #e4e4e4;
    --ink: #2b2b2b;
    --pin: #d9534f;
    --social: #3b5a9a;
  }
  * { box-sizing: border-box; margin: 0; padding: 0; }
  html, body { width: 1200px; height: 880px; overflow: hidden; }
  body { background: var(--stage); font-family: "Josefin Sans", sans-serif; }

  .brochure {
    position: absolute; left: 30px; top: 37px;
    width: 1140px; height: 805px; overflow: hidden;
    background: var(--paper);
    box-shadow: 0 6px 18px rgba(0,0,0,.25);
  }
  .brochure__art { position: absolute; inset: 0; }
  .band { position: absolute; left: 0; width: 100%; height: 11px; background: var(--orange); z-index: 5; }
  .band--top { top: 0; }
  .band--bottom { bottom: 0; }

  .panel { position: absolute; top: 0; height: 100%; width: 380px; z-index: 3; }
  .panel--about { left: 0; color: #fff; }
  .panel--contact { left: 380px; }
  .panel--cover { left: 760px; }

  .about__text {
    position: absolute; left: 35px; top: 84px; width: 308px;
    font-size: 16.5px; line-height: 26px; text-align: justify;
  }
  .about__text p + p { margin-top: 26px; }

  .pill {
    position: absolute; background: var(--green); border-radius: 24px;
    box-shadow: 0 4px 6px rgba(0,0,0,.25);
    font-family: "Sriracha", cursive; text-align: center; white-space: nowrap;
  }
  .pill--tagline { left: 22px; top: 420px; width: 320px; height: 46px; line-height: 46px; font-size: 27px; color: var(--green-dark); }
  .pill--contact { left: 71px; top: 555px; width: 235px; height: 45px; line-height: 47px; font-size: 28px; color: #fff; }

  .brand-name {
    position: absolute; left: 0; width: 100%; text-align: center;
    font-family: "Josefin Sans", sans-serif; font-weight: 700; text-transform: uppercase; line-height: 1.1;
  }
  .brand-name--about { top: 640px; font-size: 38px; color: #fff; }
  .brand-name--contact { top: 490px; font-size: 24px; color: var(--brown-text); }

  .contact__list { position: absolute; left: 0; top: 616px; width: 100%; text-align: center; list-style: none; font-size: 16.5px; color: var(--ink); }
  .contact__list li { height: 30px; line-height: 30px; }
  .contact__social-mark { display: inline-block; width: 14px; height: 14px; background: var(--social); margin-right: 6px; vertical-align: -1px; }

  .badge {
    position: absolute; left: 83px; top: 407px; width: 216px; height: 216px; border-radius: 50%;
    background: var(--paper); border: 8px solid var(--orange-soft);
    display: flex; align-items: center; justify-content: center;
  }
  .brand-name--badge { position: static; font-size: 25px; color: var(--brown-text); }

  .welcome {
    position: absolute; left: 0; top: 662px; width: 100%; text-align: center;
    font-family: "Sriracha", cursive; color: #fff; font-size: 31px; line-height: 40px;
  }
  .cover__url { position: absolute; left: 0; top: 764px; width: 100%; text-align: center; color: #fff; font-size: 14px; }
</style>
</head>
<body>
<main class="brochure">
  <svg class="brochure__art" width="1140" height="805" viewBox="0 0 1140 805">
    <defs>
      <linearGradient id="aboutPhoto" x1="0" y1="0" x2="0" y2="1">
        <stop offset="0" stop-color="#7c5226"/>
        <stop offset="0.5" stop-color="#8a5c2c"/>
        <stop offset="1" stop-color="#5e3a14"/>
      </linearGradient>
      <linearGradient id="contactPaper" x1="0" y1="0" x2="1" y2="0">
        <stop offset="0" stop-color="#e2e2e2"/>
        <stop offset="0.5" stop-color="#ffffff"/>
        <stop offset="1" stop-color="#f2f2f2"/>
      </linearGradient>
      <linearGradient id="coverPhoto" x1="0" y1="0" x2="0" y2="1">
        <stop offset="0" stop-color="#7d5a3a"/>
        <stop offset="1" stop-color="#5b3710"/>
      </linearGradient>
      <linearGradient id="heroPhoto" x1="0" y1="0" x2="1" y2="1">
        <stop offset="0" stop-color="#dde4c8"/>
        <stop offset="0.35" stop-color="#d9b690"/>
        <stop offset="0.7" stop-color="#8a6240"/>
        <stop offset="1" stop-color="#3e2a1c"/>
      </linearGradient>
      <radialGradient id="mapTone" cx="0.5" cy="0.5" r="0.5">
        <stop offset="0" stop-color="#eeeeea"/>
        <stop offset="1" stop-color="#dfe3da"/>
      </radialGradient>
    </defs>
    <rect x="0" y="0" width="380" height="805" fill="url(#aboutPhoto)" role="img" aria-label="Photo: pet owner cuddling a cat, under a brown tint"/>
    <rect x="380" y="0" width="380" height="805" fill="url(#contactPaper)"/>
    <rect x="760" y="0" width="380" height="805" fill="url(#coverPhoto)" role="img" aria-label="Photo: cat resting at home, under a brown tint"/>
    <circle cx="913" cy="212" r="333" fill="none" stroke="var(--orange)" stroke-width="14"/>
    <circle cx="913" cy="212" r="322" fill="url(#heroPhoto)" role="img" aria-label="Photo: woman lovingly holding her dog"/>
    <circle cx="574" cy="242" r="133" fill="url(#mapTone)" stroke="var(--orange)" stroke-width="6" role="img" aria-label="Street map of the local suburb showing the hospital location"/>
    <path d="M568 232 a6 6 0 1 1 12 0 c0 5 -6 12 -6 12 s-6 -7 -6 -12z" fill="var(--pin)"/>
  </svg>

  <div class="band band--top"></div>
  <div class="band band--bottom"></div>

  <section class="panel panel--about">
    <div class="about__text">
      <p>Fernvale Pets Hospital is a companion animal Veterinary Hospital in Brackenridge. We treat Dogs, Cats, Reptiles, Rodents, Birds, and other little critters.</p>
      <p>As a companion animals only Hospital, we are dedicated to improving the well-bing of your beloved pets.</p>
      <p>We think they are part of the family and should receive the absolute best possible care.</p>
    </div>
    <div class="pill pill--tagline">Fernvale Pet Hospitals</div>
    <div class="brand-name brand-name--about">Fernvale Pet<br>Hospital</div>
  </section>

  <section class="panel panel--contact">
    <div class="brand-name brand-name--contact">Fernvale Pet<br>Hospital</div>
    <div class="pill pill--contact">Contact Us</div>
    <ul class="contact__list">
      <li>14 Quorra Ct Brackenridge NSW 2418.</li>
      <li>6194 7203 | 6194 1582</li>
      <li>contact@fernvalepet.com</li>
      <li>www.fernvalepet.com</li>
      <li><span class="contact__social-mark"></span>Fernvale PetHospital</li>
    </ul>
  </section>

  <section class="panel panel--cover">
    <div class="badge"><div class="brand-name brand-name--badge">Fernvale Pet<br>Hospital</div></div>
    <div class="welcome">Welcome to<br>Fernvale Pet Hospitals</div>
    <div class="cover__url">www.fernvalepet.com</div>
  </section>
</main>
</body>
</html>
```